Business card design needed

partition walls
suspended ceilings
bulkheads
shops
office fitouts
compressed sheeting

main colour aqua blue with silver and white writing

k.r.m plastering (vic) pty.ltd

noel carrow
M:0400712864 E:krmplastering@mailvane.com
ABN: 64 203 917 482
ACN: 271 604 815

```html
<!DOCTYPE html>
<html lang="en">
<head>
<meta charset="utf-8">
<title>K.R.M Plastering (vic) pty.ltd – Business Card</title>
<link rel="stylesheet" href="https://fonts.googleapis.com/css2?family=Russo+One&family=Didact+Gothic&display=swap">
<style>
  :root {
    --aqua-light: #0ea8e6;
    --aqua-mid: #1190d6;
    --aqua-deep: #1a6fc2;
    --charcoal: #2b2b2b;
    --silver-light: #f2f2f2;
    --silver-dark: #9a9a9a;
    --white: #ffffff;
    --ink: #1d2b3c;
    --name-blue: #1d9be2;
    --rule-blue: #1a9be0;
  }
  * { margin: 0; padding: 0; box-sizing: border-box; }
  html, body {
    width: 1005px;
    height: 1200px;
    overflow: hidden;
    background: var(--white);
  }
  .canvas {
    position: relative;
    width: 1005px;
    height: 1200px;
  }
  .card {
    position: absolute;
    left: 0;
    width: 1005px;
    height: 578px;
    overflow: hidden;
    border: 1px solid #3a3a3a;
  }
  .card--front { top: 0; }
  .card--back { top: 622px; }
  .card__art {
    position: absolute;
    inset: 0;
    width: 100%;
    height: 100%;
  }
  .brand-name {
    position: absolute;
    font-family: "Didact Gothic", sans-serif;
    font-weight: 400;
    color: var(--white);
    line-height: 1.1;
    display: flex;
    align-items: center;
    gap: 16px;
  }
  .brand-name__square {
    width: 22px;
    height: 22px;
    background: var(--white);
    flex: none;
  }
  .card--front .brand-name {
    left: 40px;
    top: 240px;
    font-size: 40px;
  }
  .card--back .brand-name {
    left: 600px;
    top: 240px;
    font-size: 36px;
  }
  .contact-name {
    position: absolute;
    left: 634px;
    top: 258px;
    font-family: "Russo One", sans-serif;
    font-size: 52px;
    color: var(--name-blue);
    letter-spacing: 0.5px;
  }
  .contact-rule {
    position: absolute;
    left: 633px;
    top: 325px;
    width: 372px;
    height: 2px;
    background: var(--rule-blue);
  }
  .contact-phone {
    position: absolute;
    left: 688px;
    top: 336px;
    font-family: "Didact Gothic", sans-serif;
    font-size: 38px;
    color: var(--white);
  }
  .company-details {
    position: absolute;
    left: 32px;
    top: 470px;
    font-family: "Didact Gothic", sans-serif;
    font-size: 24px;
    line-height: 33px;
    color: var(--ink);
  }
  .services {
    position: absolute;
    left: 44px;
    top: 136px;
    list-style: none;
    font-family: "Didact Gothic", sans-serif;
    font-size: 45px;
    line-height: 52px;
    color: var(--white);
  }
  .services li::before {
    content: "* ";
    margin-right: 6px;
  }
</style>
</head>
<body>
<div class="canvas">

  <section class="card card--front">
    <svg class="card__art" viewBox="0 0 1005 578" preserveAspectRatio="none" aria-hidden="true">
      <defs>
        <radialGradient id="aquaFront" cx="0.35" cy="0.5" r="0.75">
          <stop offset="0" stop-color="var(--aqua-light)"/>
          <stop offset="0.6" stop-color="var(--aqua-mid)"/>
          <stop offset="1" stop-color="var(--aqua-deep)"/>
        </radialGradient>
        <linearGradient id="silverFront" x1="0" y1="0" x2="0" y2="1">
          <stop offset="0" stop-color="var(--silver-dark)"/>
          <stop offset="0.5" stop-color="var(--silver-light)"/>
          <stop offset="1" stop-color="var(--silver-dark)"/>
        </linearGradient>
      </defs>
      <rect width="1005" height="578" fill="url(#aquaFront)"/>
      <circle cx="944" cy="276" r="392" fill="url(#silverFront)"/>
      <circle cx="952" cy="269" r="378" fill="var(--charcoal)"/>
    </svg>

    <div class="brand-name"><span class="brand-name__square"></span>K.R.M Plastering (vic) pty.ltd</div>

    <div class="contact-name">Noel Carrow</div>
    <div class="contact-rule"></div>
    <div class="contact-phone">0400712864</div>

    <div class="company-details">
      <p>E: krmplastering@mailvane.com</p>
      <p>Abn: 64 203 917 482, Acn: 271 604 815</p>
    </div>
  </section>

  <section class="card card--back">
    <svg class="card__art" viewBox="0 0 1005 578" preserveAspectRatio="none" aria-hidden="true">
      <defs>
        <radialGradient id="aquaBack" cx="0.75" cy="0.45" r="0.5">
          <stop offset="0" stop-color="var(--aqua-light)"/>
          <stop offset="0.6" stop-color="var(--aqua-mid)"/>
          <stop offset="1" stop-color="var(--aqua-deep)"/>
        </radialGradient>
        <linearGradient id="silverBack" x1="0" y1="0" x2="0" y2="1">
          <stop offset="0" stop-color="var(--silver-dark)"/>
          <stop offset="0.5" stop-color="var(--silver-light)"/>
          <stop offset="1" stop-color="var(--silver-dark)"/>
        </linearGradient>
      </defs>
      <rect width="1005" height="578" fill="var(--charcoal)"/>
      <circle cx="944" cy="282" r="392" fill="url(#silverBack)"/>
      <circle cx="954" cy="280" r="378" fill="url(#aquaBack)"/>
    </svg>

    <ul class="services">
      <li>Partition Walls</li>
      <li>Suspended Ceilings</li>
      <li>Bulkheads</li>
      <li>Office Fitouts</li>
      <li>Shops</li>
      <li>Compressed Sheeting</li>
    </ul>

    <div class="brand-name"><span class="brand-name__square"></span><span>K.R.M Plastering<br>(vic) pty.ltd</span></div>
  </section>

</div>
</body>
</html>
```